1923 Basins & Spouts Business Card

I'm wanting to get a business card designed. Our business is 1923 Basins & Spouts
Details for the card:

1923 Basins & Spouts
Name: Gareth Vostle
Email: gareth@1923basinsandspouts.com.au
Website: www.1923basinsandspouts.com.au
Mobile: 0439 602 158
Phone: 02 5550 1843

Font of Basins & Spouts is called Snell Roundhand. Not sue what font logo text is.

I'm thinking two sided but it doesn't have to be.

```html
<!DOCTYPE html>
<html lang="en">
<head>
<meta charset="utf-8">
<title>1923 Basins &amp; Spouts – Business Card</title>
<link rel="stylesheet" href="https://fonts.googleapis.com/css2?family=Roboto:wght@400;500;700&display=swap">
<style>
  :root {
    --backdrop: #dcdde1;
    --card-dark-start: #0e0e0e;
    --card-dark-end: #2f2f2f;
    --card-light: #ffffff;
    --ink: #1f1f1f;
    --ink-on-dark: #ffffff;
    --icon-tile: #f1f1f1;
  }
  * { box-sizing: border-box; margin: 0; padding: 0; }
  html, body {
    width: 1200px;
    height: 866px;
    overflow: hidden;
    background: var(--backdrop);
    font-family: "Roboto", Arial, sans-serif;
  }
  .canvas {
    position: relative;
    width: 1200px;
    height: 866px;
  }
  .card {
    position: absolute;
    top: 221px;
    width: 293px;
    height: 456px;
    border-radius: 30px;
  }
  .card--front {
    left: 244px;
    background: linear-gradient(90deg, var(--card-dark-start) 0%, var(--card-dark-start) 35%, var(--card-dark-end) 70%, var(--card-dark-end) 100%);
  }
  .card--back {
    left: 644px;
    background: var(--card-light);
    color: var(--ink);
    text-align: center;
  }
  .brand-name {
    position: absolute;
    left: 0;
    right: 0;
    text-align: center;
    font-weight: 500;
  }
  .card--front .brand-name {
    top: 172px;
    color: var(--ink-on-dark);
    font-size: 30px;
    line-height: 1.35;
  }
  .card--back .brand-name {
    top: 100px;
    color: var(--ink);
    font-size: 20px;
    line-height: 1.3;
  }
  .holder {
    position: absolute;
    top: 218px;
    left: 0;
    right: 0;
  }
  .holder__name {
    font-size: 21px;
    font-weight: 700;
    line-height: 1.2;
  }
  .holder__role {
    font-size: 13px;
    font-weight: 500;
    margin-top: 3px;
  }
  .contact {
    position: absolute;
    top: 283px;
    left: 0;
    right: 0;
    font-size: 13px;
    line-height: 17px;
  }
  .contact__label { font-weight: 700; }
  .contact__web { margin-top: 6px; }
  .social {
    position: absolute;
    top: 380px;
    left: 50%;
    transform: translateX(-50%);
    display: flex;
    gap: 6px;
    padding: 6px 8px;
    background: var(--icon-tile);
  }
  .social__dot {
    width: 10px;
    height: 10px;
    border-radius: 50%;
    background: var(--ink);
  }
</style>
</head>
<body>
  <main class="canvas">
    <section class="card card--front" aria-label="Card front">
      <p class="brand-name">1923<br>Basins &amp; Spouts</p>
    </section>

    <section class="card card--back" aria-label="Card back">
      <p class="brand-name">1923 Basins &amp; Spouts</p>
      <div class="holder">
        <h1 class="holder__name">Gareth Vostle</h1>
        <p class="holder__role">Director</p>
      </div>
      <div class="contact">
        <p><span class="contact__label">m:</span> 0439 602 158</p>
        <p><span class="contact__label">p:</span> 02 5550 1843</p>
        <p class="contact__web">gareth@1923basinsandspouts.com.au</p>
        <p>www.1923basinsandspouts.com.au</p>
      </div>
      <div class="social" aria-label="Social media links">
        <span class="social__dot"></span>
        <span class="social__dot"></span>
      </div>
    </section>
  </main>
</body>
</html>
```